Tennis Club Marwil - Step onto the court!

Our tennis club has fallen asleep in the past 10 years and the amount of members steadily decreased. We are now a new crew of motivated players that want to bring change, good atmosphere with up to date offers to our members.
For this specific part, we are looking to attract new adult members with different training offers.
We need one flyer that we want to use for multiple occasions:
- in 2-3 versions (different colour scheme or slightly different setup of the elements)
- A sample text inserted that we can modify later on

Our current logo and home made flyer look dusty instead of sexy. We are looking for a fresh, attractive and dynamic flyer that makes people want to be part of our activities. Our club is located in German-speaking part of Switzerland. The homepage is https://tcmarwil-example.ch/ .
I attached two files:
1. The logo: Looks old school, but it necessarily needs to be part of the flyer. Use any effect you want on it to make it look more attractive.
2. The super tennis bee: This bee can be used as inspiration, but it is purely optional. It was drawn close to our club house in the early 2000s and is used as a ball-wall.

Target Market(s)

Requirements
Must have
• - in 3 versions (different colour scheme or slightly different setup of the elements)
- The logo: Looks old school, but it necessarily needs to be part of the flyer. Use any effect you want on it to make it look more attractive.
Nice to have
• The super tennis bee: This bee can be used as inspiration, but it is purely optional. It was drawn close to our club house in the early 2000s and is used as a ball-wall

```html
<!DOCTYPE html>
<html lang="en">
<head>
<meta charset="utf-8">
<title>Tennis Club Marwil – Grand Opening</title>
<link href="https://fonts.googleapis.com/css2?family=Roboto:wght@400;500;700;900&family=Roboto+Condensed:wght@700&display=swap" rel="stylesheet">
<style>
  :root{
    --teal:#1f9fc4;
    --teal-dark:#137fa1;
    --ink:#2b2f33;
    --band:#3a3e42;
    --paper:#ffffff;
    --muted:#6c737a;
    --clay:#c77a4a;
    --grass:#3f8a3a;
  }
  *{box-sizing:border-box;margin:0;padding:0}
  html,body{width:900px;height:1200px;overflow:hidden;background:#eef0f2}
  body{font-family:"Roboto",Arial,sans-serif;color:var(--ink)}
  .flyer{position:relative;width:900px;height:1200px;background:var(--paper);overflow:hidden}
  .abs{position:absolute}

  .club-mark{left:40px;top:40px;width:170px;display:flex;flex-direction:column;align-items:center;gap:10px}
  .club-mark .dot{width:110px;height:110px;border-radius:50%;background:var(--ink)}
  .club-mark .name{font-weight:700;font-size:17px;text-align:center;color:var(--ink);line-height:1.15}

  .headline{left:230px;top:36px;font-weight:900;line-height:.92;text-transform:uppercase}
  .headline .grand{font-size:96px;color:var(--teal);display:block}
  .headline .opening{font-size:96px;color:var(--ink);display:block}

  .date-box{left:700px;top:0;width:160px;height:210px;background:var(--teal);color:#fff;
    display:flex;flex-direction:column;justify-content:center;align-items:center;text-transform:uppercase;
    font-family:"Roboto Condensed",Arial,sans-serif;font-weight:700;line-height:1}
  .date-box .day{font-size:22px}
  .date-box .num{font-size:52px;margin:6px 0}
  .date-box .month{font-size:20px}
  .date-box .year{font-size:38px;margin-top:8px}

  .photo{background:linear-gradient(160deg,#8fc3df 0%,#e5d3b8 55%,var(--clay) 100%)}
  .photo-kid{left:40px;top:240px;width:500px;height:330px}
  .photo-woman{left:560px;top:240px;width:300px;height:330px;background:linear-gradient(170deg,#bfe0ee 0%,#f2f2f2 50%,#7fbf5f 100%)}
  .photo-man{left:330px;top:580px;width:240px;height:300px;background:linear-gradient(180deg,#e9eef2 0%,#cfd8de 60%,#f6f6f6 100%)}

  .challenge{left:40px;top:600px;width:280px}
  .challenge h2{font-weight:900;font-size:32px;color:var(--teal);text-transform:uppercase;line-height:1}
  .challenge .tagline{font-size:19px;color:var(--ink);margin:6px 0 22px}
  .challenge ul{list-style:none}
  .challenge li{display:flex;align-items:center;gap:12px;font-size:15px;font-weight:500;text-transform:uppercase;color:var(--ink);margin-bottom:16px}
  .challenge li::before{content:"";width:12px;height:12px;background:var(--teal);flex:none}

  .offer{left:600px;top:610px;width:270px;text-transform:uppercase;font-weight:900;line-height:.95}
  .offer .pct{font-size:110px;color:var(--teal)}
  .offer .pct small{font-size:60px}
  .offer .off{font-size:46px;color:var(--teal);display:inline-block;vertical-align:top}
  .offer .what{font-size:40px;color:var(--ink);margin-top:6px}

  .info-band{left:0;top:890px;width:900px;height:110px;background:var(--band);color:#fff;display:flex;align-items:center;padding:0 40px}
  .hours{display:flex;align-items:center;gap:14px;flex:1}
  .hours .time{font-weight:900;font-size:60px;letter-spacing:-1px}
  .hours .open{font-weight:700;font-size:22px;line-height:1.05;text-transform:uppercase}
  .hours .open span{color:var(--teal);display:block}
  .pickup{display:flex;align-items:center;gap:16px}
  .pickup .label{border:3px solid #fff;padding:6px 12px;font-weight:900;font-size:22px;line-height:1;text-transform:uppercase}

  .contacts{left:40px;top:1020px;width:820px;display:flex;justify-content:space-between;align-items:center}
  .contact{display:flex;align-items:center;gap:12px;font-weight:700;font-size:26px;color:var(--ink)}
  .contact .ico{width:44px;height:44px;border-radius:50%;background:var(--teal);display:flex;align-items:center;justify-content:center}
  .contact.web{font-size:22px}

  .cta-strip{left:40px;top:1095px;width:400px;height:32px;background:var(--teal);color:#fff;font-size:14px;font-weight:700;text-transform:uppercase;display:flex;align-items:center;padding-left:16px;letter-spacing:.5px}
  .address{left:480px;top:1100px;font-size:14px;color:var(--muted)}
  .grass{left:0;top:1140px;width:900px;height:60px;background:linear-gradient(180deg,#6fb24f 0%,var(--grass) 100%)}
</style>
</head>
<body>
<main class="flyer">
  <div class="abs club-mark">
    <div class="dot"></div>
    <div class="name">Tennis Club Marwil</div>
  </div>

  <h1 class="abs headline"><span class="grand">Grand</span><span class="opening">Opening</span></h1>

  <div class="abs date-box">
    <span class="day">Friday</span>
    <span class="num">31st</span>
    <span class="month">December</span>
    <span class="year">2021</span>
  </div>

  <div class="abs photo photo-kid" role="img" aria-label="Young player hitting a ball on a clay tennis court"></div>
  <div class="abs photo photo-woman" role="img" aria-label="Woman holding a tennis racket outdoors"></div>
  <div class="abs photo photo-man" role="img" aria-label="Man standing with a tennis racket"></div>

  <section class="abs challenge">
    <h2>Tennis Challenge</h2>
    <p class="tagline">Your ideal fitness place</p>
    <ul>
      <li>Group adult lessons</li>
      <li>Small team training</li>
      <li>Evening matches</li>
      <li>Private coaching</li>
    </ul>
  </section>

  <section class="abs offer">
    <div><span class="pct">10<small>%</small></span> <span class="off">Off</span></div>
    <div class="what">On tennis coaching</div>
  </section>

  <section class="abs info-band">
    <div class="hours">
      <span class="time">9-16</span>
      <span class="open"><span>Open to</span>everyone</span>
    </div>
    <div class="pickup">
      <svg width="60" height="44" viewBox="0 0 60 44" aria-hidden="true">
        <rect x="2" y="4" width="52" height="30" rx="4" fill="none" stroke="#fff" stroke-width="3"/>
        <rect x="8" y="9" width="12" height="10" fill="#fff"/>
        <rect x="23" y="9" width="12" height="10" fill="#fff"/>
        <rect x="38" y="9" width="12" height="10" fill="#fff"/>
        <circle cx="14" cy="36" r="5" fill="#fff"/>
        <circle cx="42" cy="36" r="5" fill="#fff"/>
      </svg>
      <span class="label">Pickup<br>&amp; Drop</span>
    </div>
  </section>

  <div class="abs contacts">
    <div class="contact">
      <span class="ico">
        <svg width="22" height="22" viewBox="0 0 24 24" aria-hidden="true"><path fill="#fff" d="M6.6 10.8a15.1 15.1 0 0 0 6.6 6.6l2.2-2.2c.3-.3.7-.4 1-.2 1.1.4 2.3.6 3.6.6.6 0 1 .4 1 1V20c0 .6-.4 1-1 1A17 17 0 0 1 3 4c0-.6.4-1 1-1h3.5c.6 0 1 .4 1 1 0 1.3.2 2.5.6 3.6.1.3 0 .7-.2 1z"/></svg>
      </span>
      079 555 01 23
    </div>
    <div class="contact web">
      <span class="ico">
        <svg width="22" height="22" viewBox="0 0 24 24" aria-hidden="true"><circle cx="12" cy="12" r="9" fill="none" stroke="#fff" stroke-width="2"/><path d="M3 12h18M12 3c3 3 3 15 0 18M12 3c-3 3-3 15 0 18" fill="none" stroke="#fff" stroke-width="2"/></svg>
      </span>
      https://tcmarwil-example.ch/
    </div>
  </div>

  <div class="abs cta-strip">Contact us for more information</div>
  <div class="abs address">Step onto the court! · Marwil clubhouse courts</div>

  <div class="abs grass" role="img" aria-label="Strip of green grass"></div>
</main>
</body>
</html>
```